Technology Charity needs a Web Design

Vendra Lum purchases used company mobiles and donates the proceeds to charity. It is showing companies how they can do social good, with unused technology. We would like to see designs with relevant images of social good. Open to ideas, and more is explained in the attached brief. Logo is attached as well.

```html
<!DOCTYPE html>
<html lang="en">
<head>
<meta charset="utf-8">
<title>Vendra Lum – Tech for social good</title>
<link rel="stylesheet" href="https://fonts.googleapis.com/css2?family=Poppins:wght@400;500;600;700&display=swap">
<style>
:root{
  --sage:#c5c8a2;
  --sage-bg:#c6c8a1;
  --slate:#8eafba;
  --slate-dark:#6f96a3;
  --ink:#222222;
  --body:#666666;
  --white:#ffffff;
  --footer:#3a3a3a;
}
*{box-sizing:border-box;margin:0;padding:0}
html,body{width:1200px;height:4773px;overflow:hidden}
body{font-family:"Poppins",sans-serif;color:var(--ink);background:var(--white);position:relative}
section,header,footer{position:absolute;left:0;width:1200px}
.abs{position:absolute}
.btn{position:absolute;width:174px;height:50px;background:var(--sage);color:var(--white);font-size:16px;font-weight:600;display:flex;align-items:center;justify-content:center;gap:8px;text-transform:uppercase}
.btn .dot{width:14px;height:14px;border-radius:50%;background:var(--white);position:relative}
.btn .dot::after{content:"";position:absolute;left:4px;top:4px;width:4px;height:4px;border-top:2px solid var(--sage);border-right:2px solid var(--sage);transform:rotate(45deg)}

/* header */
.site-header{top:0;height:87px;border-top:4px solid var(--slate);background:var(--white)}
.brand{left:144px;top:22px;display:flex;align-items:center;gap:12px;font-size:34px;font-weight:500;color:var(--slate-dark);line-height:1}
.brand-mark{width:22px;height:22px;background:var(--sage)}
.main-nav{left:500px;top:33px;display:flex;gap:22px;font-size:14px;font-weight:500}
.main-nav .active{color:var(--slate-dark)}

/* hero */
.hero{top:87px;height:635px}
.hero-photo{position:absolute;inset:0;background:linear-gradient(110deg,#d2c7c4 0%,#8c8c97 30%,#3c5566 55%,#6c8aa0 75%,#243644 100%)}
.hero-photo::after{content:"";position:absolute;left:0;bottom:0;width:420px;height:360px;background:radial-gradient(circle at 0% 100%,rgba(232,120,40,.75),rgba(232,120,40,0) 70%)}
.hero-title{top:170px;width:100%;text-align:center;font-size:78px;font-weight:700;color:var(--white)}
.hero-lead{top:270px;width:100%;text-align:center;font-size:24px;font-weight:500;color:var(--white);line-height:36px}
.slider-dots{left:1130px;top:258px;display:flex;flex-direction:column;gap:12px}
.slider-dots span{width:10px;height:10px;border-radius:50%;background:var(--white)}

/* what we do */
.what{top:722px;height:658px}
.what-photo{left:0;top:0;width:518px;height:658px;background:linear-gradient(135deg,#cfd8e0,#5c7a96 55%,#e8e2da)}
.section-title{font-size:48px;font-weight:700;color:var(--ink)}
.what h2{left:606px;top:88px}
.what p{left:606px;top:180px;width:452px;font-size:13px;line-height:31px;color:var(--body)}
.what .btn{left:606px;top:504px}

/* benefits */
.benefits{top:1380px;height:1004px;background:var(--sage-bg)}
.benefits h2{top:104px;width:100%;text-align:center;font-size:50px}
.benefits .intro{top:200px;width:100%;text-align:center;font-size:13px;line-height:31px;color:#5e5e4e}
.card{position:absolute;width:292px;height:276px;background:var(--white);text-align:center;padding-top:24px}
.card svg{width:54px;height:46px}
.card h3{font-size:18px;font-weight:500;line-height:25px;margin-top:10px;height:54px;display:flex;align-items:center;justify-content:center}
.card p{font-size:12px;line-height:22px;color:var(--body);margin:10px 28px 0;height:46px;overflow:hidden}
.card .more{display:block;margin-top:16px;font-size:15px;font-weight:600;color:var(--slate-dark)}

/* how it works */
.how{top:2384px;height:857px;background:var(--slate);color:var(--white)}
.how h2{top:80px;width:100%;text-align:center;font-size:50px;font-weight:700}
.how .intro{top:160px;width:100%;text-align:center;font-size:13px}
.steps{position:absolute;left:0;top:0}
.step-num{position:absolute;width:240px;text-align:center;font-size:42px;font-weight:600;color:rgba(255,255,255,.85)}
.step-text{position:absolute;width:220px;text-align:center;font-size:12px;line-height:20px}

/* contact */
.contact{top:3241px;height:658px}
.contact h2{left:143px;top:82px}
.contact .intro{left:143px;top:154px;font-size:13px;color:var(--body)}
.field{position:absolute;height:54px;border:2px solid #bdbdbd;font-size:13px;color:#555;padding:0 24px;display:flex;align-items:center;justify-content:space-between}
.contact .btn{left:144px;top:515px}
.contact-photo{left:683px;top:0;width:517px;height:658px;background:linear-gradient(160deg,#8a6c55,#c7b29a 40%,#3e4e5f 80%,#2b3340)}

/* mission */
.mission{top:3899px;height:657px}
.mission-photo{position:absolute;inset:0;background:linear-gradient(120deg,#3d4c58 0%,#56626c 45%,#8d949a 75%,#c7c9cc 100%)}
.mission-photo::after{content:"";position:absolute;inset:0;background:rgba(30,40,50,.35)}
.mission h2{top:180px;width:100%;text-align:center;font-size:48px;font-weight:700;color:var(--white)}
.mission p{top:278px;left:170px;width:860px;text-align:center;font-size:13px;line-height:32px;color:var(--white)}
.mission .btn{left:513px;top:414px}

/* footer */
.site-footer{top:4556px;height:217px;background:var(--footer);color:var(--white);text-align:center}
.social{position:absolute;top:42px;left:532px;display:flex;gap:6px}
.social span{width:30px;height:30px;border:2px solid var(--white);border-radius:50%}
.foot-nav{position:absolute;top:100px;width:100%;display:flex;justify-content:center;gap:28px;font-size:17px;font-weight:600}
.copy{position:absolute;top:150px;width:100%;font-size:14px}
</style>
</head>
<body>

<header class="site-header">
  <div class="abs brand"><span class="brand-mark"></span>vendra lum</div>
  <nav class="abs main-nav">
    <span class="active">What we do</span><span>Benefits</span><span>How Does It Work?</span><span>Contact Us</span><span>Our Mission</span>
  </nav>
</header>

<section class="hero">
  <div class="hero-photo" role="img" aria-label="Business people silhouetted against glass office towers at sunset"></div>
  <h1 class="abs hero-title">Vendra Lum</h1>
  <p class="abs hero-lead">Vendra Lum offers an easy and economical<br>solution to the issue of used mobiles.</p>
  <a class="btn" style="left:513px;top:400px">Get Started <span class="dot"></span></a>
  <div class="abs slider-dots"><span></span><span></span><span></span><span></span><span></span></div>
</section>

<section class="what">
  <div class="abs what-photo" role="img" aria-label="Smiling colleagues working together in a bright office"></div>
  <h2 class="abs section-title">What We Do</h2>
  <p class="abs">Vendra Lum creates an easy pathway for organisations, to become more sustainable, renewable and give back to the community. We do this by purchasing used employee mobiles, and donating the proceeds to social good, on behalf of organisations. Helping organisation give to meaningful causes that do so much for the community.Many organisations aren't sure what to do with their used mobiles. They either store them in a back room, or have vague, ineffective solutions, such as employee buy-back schemes, or passing on used mobiles to employees.</p>
  <a class="btn">Read More <span class="dot"></span></a>
</section>

<section class="benefits">
  <h2 class="abs section-title">Benefits to Your Organisation</h2>
  <p class="abs intro">If you are an organisation with a desire to make the world a better place, we can help you.<br>Re-purposing used technology has incredible benefits such as:</p>

  <div class="card" style="left:146px;top:320px">
    <svg viewBox="0 0 54 46"><g fill="#a8aa85"><circle cx="27" cy="12" r="8"/><circle cx="12" cy="16" r="6"/><circle cx="42" cy="16" r="6"/><path d="M14 44c0-10 6-16 13-16s13 6 13 16z"/><path d="M2 40c0-8 4-12 10-12 3 0 5 1 6 2-3 3-5 6-5 10z"/><path d="M52 40c0-8-4-12-10-12-3 0-5 1-6 2 3 3 5 6 5 10z"/></g></svg>
    <h3>Improve organisational<br>Reputation</h3>
    <p>Individuals and communities have great respect for organisations</p>
    <span class="more">READ MORE</span>
  </div>
  <div class="card" style="left:454px;top:320px">
    <svg viewBox="0 0 54 46"><g fill="none" stroke="#a8aa85" stroke-width="5"><path d="M11 21a16 16 0 0 1 29-8"/><path d="M43 25a16 16 0 0 1-29 8"/></g><path d="M35 6l10 1-2 11z M19 40l-10-1 2-11z" fill="#a8aa85"/></svg>
    <h3>Provide a simple &amp; effective<br>channel for re-use.</h3>
    <p>We make it easier to clear outdated stock, paving the way for new</p>
    <span class="more">READ MORE</span>
  </div>
  <div class="card" style="left:763px;top:320px">
    <svg viewBox="0 0 54 46"><path d="M8 40C8 18 24 8 46 8c2 20-10 32-30 30z" fill="#a8aa85"/><path d="M6 44c8-12 18-20 30-26" stroke="#fff" stroke-width="3" fill="none"/></svg>
    <h3>Environmentally<br>friendly</h3>
    <p>By repurposing used mobiles, for reuse or recycling, extends</p>
    <span class="more">READ MORE</span>
  </div>
  <div class="card" style="left:146px;top:613px">
    <svg viewBox="0 0 54 46"><path d="M6 6h18l22 22-16 16L8 22z" fill="#a8aa85"/><circle cx="15" cy="15" r="3.5" fill="#fff"/><path d="M28 4l22 22" stroke="#a8aa85" stroke-width="3"/></svg>
    <h3>Offer benefits for<br>your brand</h3>
    <p>Customers are willing to pay premium rates for goods from</p>
    <span class="more">READ MORE</span>
  </div>
  <div class="card" style="left:454px;top:613px">
    <svg viewBox="0 0 54 46"><g fill="#a8aa85"><path d="M27 2l24 10H3z"/><rect x="4" y="14" width="46" height="4"/><rect x="8" y="20" width="5" height="18"/><rect x="18" y="20" width="5" height="18"/><rect x="31" y="20" width="5" height="18"/><rect x="41" y="20" width="5" height="18"/><rect x="2" y="40" width="50" height="5"/></g></svg>
    <h3>Boost company<br>morale</h3>
    <p>People are happier when working at socially responsible companies</p>
    <span class="more">READ MORE</span>
  </div>
  <div class="card" style="left:763px;top:613px">
    <svg viewBox="0 0 54 46"><g fill="none" stroke="#a8aa85" stroke-width="4"><path d="M3 2v41h49"/><path d="M9 34l12-12 8 8 16-16"/></g><path d="M38 10h11v11z" fill="#a8aa85"/></svg>
    <h3>Entice millenials</h3>
    <p>They account for the largest percentage of the global workforce and drive trillions of dollars</p>
    <span class="more">READ MORE</span>
  </div>
</section>

<section class="how">
  <h2 class="abs">How does it work?</h2>
  <p class="abs intro">It is simple and easy, with these simple steps</p>
  <svg class="steps" width="1200" height="857" viewBox="0 0 1200 857">
    <g fill="none" stroke="rgba(255,255,255,.6)" stroke-width="4" stroke-dasharray="520 234">
      <circle cx="328" cy="376" r="120" transform="rotate(-34 328 376)"/>
      <circle cx="600" cy="372" r="120" transform="rotate(146 600 372)"/>
      <circle cx="870" cy="380" r="120" transform="rotate(-34 870 380)"/>
      <circle cx="343" cy="644" r="120" transform="rotate(146 343 644)"/>
      <circle cx="611" cy="636" r="120" transform="rotate(-34 611 636)"/>
      <circle cx="870" cy="644" r="120" transform="rotate(146 870 644)"/>
    </g>
  </svg>
  <div class="step-num" style="left:208px;top:288px">1</div>
  <p class="step-text" style="left:218px;top:356px">Contact Vendra Lum directly by calling xxx, or by completing your details on our form (Click here) and we will contact you.</p>

  <p class="step-text" style="left:490px;top:312px">Vendra Lum employee can either visit your office to review the stock, or you can send a listing of the mobile model numbers.</p>
  <div class="step-num" style="left:480px;top:404px">2</div>

  <div class="step-num" style="left:750px;top:294px">3</div>
  <p class="step-text" style="left:760px;top:360px">Vendra Lum provides you with an estimated voluation, with a listing of the stock.</p>

  <p class="step-text" style="left:241px;top:570px">Once this is agreed upon, you nominate the charity you would like the money to go towards, or alternatively we pay you directly. This is all agreed in writing.</p>
  <div class="step-num" style="left:223px;top:670px">4</div>

  <div class="step-num" style="left:491px;top:554px">5</div>
  <p class="step-text" style="left:501px;top:616px">Payment is made to nominated charity by Vendra Lum, on behalf of you. This is stated to the charity. Alternatively, we pay you directly for the stock.</p>

  <p class="step-text" style="left:760px;top:570px">Vendra Lum arranges pick-up of the stock.<br>NB: Our employees are young people, mainly students.</p>
  <div class="step-num" style="left:750px;top:660px">6</div>
</section>

<section class="contact">
  <h2 class="abs section-title">Contact Us</h2>
  <p class="abs intro">Complete the form below and Vendra Lum will contact you.</p>
  <div class="field" style="left:143px;top:216px;width:237px">Organisation Name:</div>
  <div class="field" style="left:387px;top:216px;width:237px">Address</div>
  <div class="field" style="left:143px;top:285px;width:237px">Main Contact Name</div>
  <div class="field" style="left:387px;top:285px;width:237px">Email</div>
  <div class="field" style="left:143px;top:352px;width:481px">Phone Number</div>
  <div class="field" style="left:143px;top:419px;width:481px">Attachments
    <svg width="22" height="22" viewBox="0 0 22 22"><path d="M15 6l-8 8a2.5 2.5 0 0 0 4 4l8-8a4.5 4.5 0 0 0-7-7l-8 8a6 6 0 0 0 9 9l6-6" fill="none" stroke="#999" stroke-width="1.6"/></svg>
  </div>
  <a class="btn">Submit <span class="dot"></span></a>
  <div class="abs contact-photo" role="img" aria-label="Two smiling students walking outdoors with backpacks"></div>
</section>

<section class="mission">
  <div class="mission-photo" role="img" aria-label="Person typing on a laptop at a desk"></div>
  <h2 class="abs">Our Mission</h2>
  <p class="abs">There are thousands of mobiles lying around in offices around Australia. The IT department tend to be at a loss of what to do with them. Most just get taken by the once-waste collections. Vendra Lum offers a solution to pay for the recycle and give the proceeds to Social Good. Now that back room full of used technology, is your company's pathway to social good.</p>
  <a class="btn">Read More <span class="dot"></span></a>
</section>

<footer class="site-footer">
  <div class="social"><span></span><span></span><span></span><span></span></div>
  <nav class="foot-nav"><span>WHAT WE DO</span><span>BENEFITS</span><span>HOW DOES IT WORK?</span><span>CONTACT US</span><span>OUR MISSION</span></nav>
  <p class="copy">© 2020 Vendra Lum . All Rights Reserved &nbsp;|&nbsp; Privacy Policy</p>
</footer>

</body>
</html>
```